Karvelin PowerPoint Templates

We need a cover page and body page templates for a complete Powerpoint presentation. We administer workers' compensation claims in California mostly to public entities. We offer cloud based software to develop and communicate all the data for each claim. Although we are a technology company, we also see ourselves as the human interface working closely with the client and injured workers.
It all starts with our Logo!
We want to loosely relate our Powerpoint design with our Logo. Maybe just in the color! WE DONT WANT TO RECREATE OUR LOGO AS A PROPOSAL . I've posted the logo and a rough proposal page for reference. We designed it using ArtHive and feel the designer met our criteria very well. As I recall the spec for the logo was to use our name and incorporate "modern, professional and personal" into the design. We will use this template to attract new business. We will be approaching a variety of industries and want the template to be designed specifically for our business identity rather than for clients we are pursuing.
I will also post a simple example of a competitor's PowerPoint presentation for reference.
Please feel free to ask any questions you may have.
Thank You!
Harold

```html
<!DOCTYPE html>
<html lang="en">
<head>
<meta charset="utf-8">
<title>Karvelin – Overview</title>
<link rel="stylesheet" href="https://fonts.googleapis.com/css2?family=Open+Sans:wght@400;600;700&display=swap">
<style>
  :root {
    --paper: #f3f3f2;
    --paper-edge: #e6e7e8;
    --tile-blue: #c9d6e6;
    --orange: #f7941d;
    --orange-light: #f9a640;
    --blue: #1e9ad6;
    --blue-light: #39aee3;
    --green: #72c02c;
    --green-light: #86cf3e;
    --shadow: #9a9a9a;
    --brand-grey: #7b7e82;
    --tagline: #3d3f42;
    --label: #ffffff;
  }
  * { margin: 0; padding: 0; box-sizing: border-box; }
  html, body { width: 1200px; height: 900px; overflow: hidden; }
  body { font-family: "Open Sans", Arial, sans-serif; background: var(--paper); }
  .slide { position: relative; width: 1200px; height: 900px; overflow: hidden; }
  .backdrop {
    position: absolute; inset: 0;
    background:
      radial-gradient(ellipse 520px 200px at 680px 250px, rgba(201,214,230,0.55), transparent 70%),
      radial-gradient(ellipse 560px 180px at 720px 650px, rgba(201,214,230,0.5), transparent 70%),
      radial-gradient(ellipse 260px 140px at 1110px 560px, rgba(201,214,230,0.45), transparent 70%),
      linear-gradient(180deg, var(--paper) 0%, var(--paper-edge) 100%);
  }
  .brand { position: absolute; top: 4px; right: 0; width: 250px; text-align: center; }
  .brand-name {
    font-weight: 600; font-size: 54px; line-height: 1; color: var(--brand-grey);
    letter-spacing: -1px; padding-top: 30px;
  }
  .brand-tagline { font-size: 16px; color: var(--tagline); margin-top: 6px; white-space: nowrap; }
  .topics { position: absolute; inset: 0; }
  .topic-label {
    font-family: "Open Sans", Arial, sans-serif; font-weight: 700; font-size: 33px;
    fill: var(--label); text-anchor: middle;
  }
</style>
</head>
<body>
<main class="slide">
  <div class="backdrop" role="img" aria-label="Faint blue mosaic of tiles sweeping across a light textured background"></div>

  <div class="brand">
    <div class="brand-name">Karvelin</div>
    <div class="brand-tagline">Claims Management Solutions</div>
  </div>

  <svg class="topics" width="1200" height="900" viewBox="0 0 1200 900">
    <defs>
      <filter id="soft-shadow" x="-50%" y="-100%" width="200%" height="300%">
        <feGaussianBlur stdDeviation="9"/>
      </filter>
      <radialGradient id="orange-fill" cx="50%" cy="45%" r="55%">
        <stop offset="0%" stop-color="var(--orange-light)"/>
        <stop offset="85%" stop-color="var(--orange-light)"/>
        <stop offset="100%" stop-color="var(--orange)"/>
      </radialGradient>
      <radialGradient id="blue-fill" cx="50%" cy="45%" r="55%">
        <stop offset="0%" stop-color="var(--blue-light)"/>
        <stop offset="85%" stop-color="var(--blue-light)"/>
        <stop offset="100%" stop-color="var(--blue)"/>
      </radialGradient>
      <radialGradient id="green-fill" cx="50%" cy="45%" r="55%">
        <stop offset="0%" stop-color="var(--green-light)"/>
        <stop offset="85%" stop-color="var(--green-light)"/>
        <stop offset="100%" stop-color="var(--green)"/>
      </radialGradient>
    </defs>

    <g class="topic-shadows" fill="var(--shadow)" opacity="0.45" filter="url(#soft-shadow)">
      <ellipse cx="200" cy="580" rx="130" ry="32"/>
      <ellipse cx="598" cy="580" rx="130" ry="32"/>
      <ellipse cx="1000" cy="580" rx="130" ry="32"/>
    </g>

    <g class="topic topic-who">
      <ellipse cx="207" cy="357" rx="184" ry="160" fill="url(#orange-fill)"/>
      <text class="topic-label" x="198" y="361">WHO WE ARE</text>
    </g>
    <g class="topic topic-what">
      <ellipse cx="596" cy="357" rx="184" ry="161" fill="url(#blue-fill)"/>
      <text class="topic-label" x="595" y="357">WHAT WE DO</text>
    </g>
    <g class="topic topic-mission">
      <ellipse cx="989" cy="357" rx="187" ry="160" fill="url(#green-fill)"/>
      <text class="topic-label" x="988" y="355">OUR MISSION</text>
    </g>
  </svg>
</main>
</body>
</html>
```